Apartment Investor Business Card Design

Need a new business card designed for my multifamily investment company

Industry/Entity Type

Real Estate

Contact Information for Business Card

Garrick Pelham - President & CEO
Brightwold Holdings, LLC
4838 North 92nd Avenue, Ste 500
Omaha, NE 68999
(402) 555-0147
Garrick@brightwoldholdings.example
Www.BrightwoldHoldings.example

Colors
3176b5

```html
<!DOCTYPE html>
<html lang="en">
<head>
<meta charset="utf-8">
<title>Brightwold Holdings Business Card</title>
<link href="https://fonts.googleapis.com/css2?family=Marcellus&display=swap" rel="stylesheet">
<style>
  :root {
    --backdrop: #2b2b2b;
    --brand-blue: #3176b5;
    --brand-blue-deep: #2a63a0;
    --card-white: #f4f4f4;
    --card-grey: #e4e4e4;
    --ink: #333333;
    --divider: #9a9a9a;
    --white: #ffffff;
  }
  * { margin: 0; padding: 0; box-sizing: border-box; }
  html, body {
    width: 1200px;
    height: 575px;
    overflow: hidden;
    background: var(--backdrop);
    font-family: "Marcellus", Georgia, serif;
  }
  .canvas { position: relative; width: 1200px; height: 575px; }

  .card {
    position: absolute;
    top: 138px;
    width: 485px;
    height: 292px;
    border-radius: 14px;
    overflow: hidden;
  }

  /* Front */
  .card-front {
    left: 81px;
    background: linear-gradient(180deg, #3a78b6 0%, var(--brand-blue-deep) 100%);
    color: var(--white);
    text-align: center;
  }
  .front-mark {
    position: absolute;
    top: 138px;
    left: 50%;
    width: 14px;
    height: 14px;
    margin-left: -7px;
    background: var(--white);
  }
  .front-name {
    position: absolute;
    top: 170px;
    left: 0;
    right: 0;
    font-size: 26px;
    font-weight: 400;
    letter-spacing: 1px;
    text-transform: uppercase;
    white-space: nowrap;
  }
  .front-web {
    position: absolute;
    top: 210px;
    left: 0;
    right: 0;
    font-size: 14px;
    letter-spacing: 2px;
  }

  /* Back */
  .card-back {
    left: 602px;
    background: linear-gradient(160deg, var(--white) 0%, var(--card-white) 55%, var(--card-grey) 100%);
    color: var(--ink);
  }
  .back-decoration {
    position: absolute;
    top: 20px;
    right: 20px;
    width: 150px;
    height: 200px;
    background: linear-gradient(180deg, rgba(200,200,200,0.35), rgba(230,230,230,0));
  }
  .back-brand {
    position: absolute;
    top: 158px;
    left: 8px;
    width: 200px;
    text-align: center;
    font-size: 10.5px;
    color: var(--ink);
    text-transform: uppercase;
    letter-spacing: 0.2px;
    white-space: nowrap;
  }
  .back-brand-mark {
    display: block;
    width: 12px;
    height: 12px;
    margin: 0 auto 10px;
    background: var(--brand-blue);
  }
  .back-divider {
    position: absolute;
    left: 214px;
    top: 69px;
    width: 1px;
    height: 127px;
    background: var(--divider);
  }
  .contact-block {
    position: absolute;
    left: 231px;
    top: 78px;
  }
  .person-name {
    font-size: 19px;
    font-weight: 400;
    color: var(--brand-blue);
    text-transform: uppercase;
    letter-spacing: 0.5px;
  }
  .person-title {
    font-size: 13px;
    color: var(--ink);
    margin-top: 2px;
  }
  .contact-list {
    list-style: none;
    margin-top: 15px;
    font-size: 11.5px;
    color: var(--ink);
  }
  .contact-list li {
    display: flex;
    align-items: center;
    height: 17.5px;
    white-space: nowrap;
  }
  .contact-list svg { width: 11px; height: 11px; margin-right: 8px; fill: var(--brand-blue-deep); flex: none; }
  .contact-list .web-highlight { color: var(--brand-blue); }

  .address-band {
    position: absolute;
    left: 0;
    right: 0;
    bottom: 0;
    height: 31px;
    background: var(--brand-blue-deep);
    color: var(--white);
    font-size: 12px;
    line-height: 31px;
    text-align: center;
  }
</style>
</head>
<body>
<main class="canvas">
  <section class="card card-front">
    <span class="front-mark"></span>
    <h1 class="front-name">Brightwold Holdings, LLC</h1>
    <p class="front-web">www.BrightwoldHoldings.example</p>
  </section>

  <section class="card card-back">
    <div class="back-decoration" role="img" aria-label="Faint city skyline decoration"></div>
    <div class="back-brand"><span class="back-brand-mark"></span>Brightwold Holdings, LLC</div>
    <div class="back-divider"></div>
    <div class="contact-block">
      <h2 class="person-name">Garrick Pelham</h2>
      <p class="person-title">President &amp; CEO</p>
      <ul class="contact-list">
        <li>
          <svg viewBox="0 0 12 12"><path d="M1 3.5C1 2 2.5 1 6 1s5 1 5 2.5v1H8.5V3.5h-5v1H1z"/><rect x="2.5" y="5.5" width="7" height="5" rx="1"/></svg>
          (402) 555-0147
        </li>
        <li>
          <svg viewBox="0 0 12 12"><rect x="1" y="2.5" width="10" height="7"/><path d="M1 2.5l5 4 5-4" stroke="#fff" stroke-width="1" fill="none"/></svg>
          Garrick@brightwoldholdings.example
        </li>
        <li>
          <svg viewBox="0 0 12 12"><circle cx="6" cy="6" r="5"/><path d="M1 6h10M6 1c-2.5 3-2.5 7 0 10M6 1c2.5 3 2.5 7 0 10" stroke="#fff" stroke-width="0.8" fill="none"/></svg>
          <span>www.<span class="web-highlight">BrightwoldHoldings</span>.example</span>
        </li>
      </ul>
    </div>
    <p class="address-band">4838 North 92nd Avenue, Ste 500 Omaha, NE 68999</p>
  </section>
</main>
</body>
</html>
```